Maple Ridge business card design

Card needs to include the following text/items:
Company Logo
Rupert Hollis
Phone # - 517-386-9042
service@mapleridgelandscaping.example
Lawn & landscape maintenance services

```html
<!DOCTYPE html>
<html lang="en">
<head>
<meta charset="utf-8">
<title>Maple Ridge Landscaping – Business Card</title>
<link rel="stylesheet" href="https://fonts.googleapis.com/css2?family=Cinzel:wght@600&family=Crimson+Text:wght@400&display=swap">
<style>
  :root {
    --backdrop: #2a2a2a;
    --paper: #f1f1f0;
    --forest: #1d3524;
    --olive: #6e8b2c;
    --ink: #1c2a20;
    --band-text: #eef0ea;
    --logo-sky: #5fb3d9;
    --logo-green: #3f6f36;
  }
  * { margin: 0; padding: 0; box-sizing: border-box; }
  html, body { width: 1200px; height: 1138px; overflow: hidden; }
  body { background: var(--backdrop); position: relative; font-family: "Crimson Text", Georgia, serif; }

  .card {
    position: absolute; width: 622px; height: 376px;
    background: var(--paper); border-radius: 16px; overflow: hidden;
  }
  .card-front { left: 272px; top: 184px; }
  .card-back { left: 274px; top: 606px; }

  .logo-area {
    position: absolute; border-radius: 50%;
    background: radial-gradient(circle at 50% 30%, var(--logo-sky) 0%, var(--logo-green) 70%);
    border: 3px solid var(--olive);
  }
  .card-front .logo-area { width: 172px; height: 172px; left: 225px; top: 30px; }
  .card-back .logo-area { width: 184px; height: 184px; left: 50px; top: 90px; }

  .brand-name {
    position: absolute; font-family: "Cinzel", "Times New Roman", serif; font-weight: 600;
    color: var(--ink); white-space: nowrap; letter-spacing: 0.5px;
  }
  .card-front .brand-name { left: 0; right: 0; top: 212px; text-align: center; font-size: 38px; }
  .card-back .brand-name { right: 29px; top: 60px; font-size: 32px; }

  .tagline-band {
    position: absolute; color: var(--band-text); font-size: 17px;
    display: flex; align-items: center; white-space: nowrap;
  }
  .card-front .tagline-band { left: 0; right: 0; top: 296px; height: 35px; background: var(--forest); justify-content: center; }
  .card-back .tagline-band { left: 290px; right: 0; top: 306px; height: 42px; background: var(--olive); justify-content: flex-end; padding-right: 29px; }

  .web-line {
    position: absolute; left: 0; right: 0; top: 336px; height: 24px;
    display: flex; align-items: center; justify-content: center; gap: 20px;
    font-size: 17px; color: var(--ink); white-space: nowrap;
  }
  .web-line .rule { width: 52px; height: 2px; background: var(--ink); }

  .back-panel { position: absolute; left: 0; top: 0; }

  .person-name { position: absolute; right: 29px; top: 150px; font-size: 28px; color: var(--ink); white-space: nowrap; }
  .contact-list { position: absolute; right: 29px; top: 196px; list-style: none; }
  .contact-list li {
    display: flex; align-items: center; justify-content: flex-end; gap: 10px;
    height: 25px; font-size: 14px; color: var(--ink); white-space: nowrap;
  }
  .contact-list svg { width: 14px; height: 14px; fill: var(--olive); flex: none; }
</style>
</head>
<body>

<section class="card card-front">
  <div class="logo-area" role="img" aria-label="Company emblem area: landscape scene with trees and sun"></div>
  <div class="brand-name">Maple Ridge</div>
  <div class="tagline-band">Lawn &amp; Landscape Maintenance Services</div>
  <div class="web-line"><span class="rule"></span><span>www.mapleridgelandscaping.example</span><span class="rule"></span></div>
</section>

<section class="card card-back">
  <svg class="back-panel" width="622" height="376" viewBox="0 0 622 376">
    <path d="M0 0 H232 C352 110 352 270 258 376 H0 Z" fill="var(--olive)"/>
    <path d="M0 0 H232 C336 110 336 260 228 376 H0 Z" fill="var(--forest)"/>
  </svg>
  <div class="logo-area" role="img" aria-label="Company emblem area: landscape scene with trees and sun"></div>
  <div class="brand-name">Maple Ridge</div>
  <div class="person-name">Rupert Hollis</div>
  <ul class="contact-list">
    <li>517-386-9042
      <svg viewBox="0 0 16 16"><path d="M2 6 C2 3 14 3 14 6 L12 7 L11 5.5 H5 L4 7 Z M4 8 H12 L13 13 H3 Z"/></svg></li>
    <li>www.mapleridgelandscaping.example
      <svg viewBox="0 0 16 16"><circle cx="8" cy="8" r="6.5" fill="none" stroke="var(--olive)" stroke-width="1.5"/><path d="M1.5 8 H14.5 M8 1.5 V14.5" stroke="var(--olive)" stroke-width="1.2"/><ellipse cx="8" cy="8" rx="3" ry="6.5" fill="none" stroke="var(--olive)" stroke-width="1.2"/></svg></li>
    <li>service@mapleridgelandscaping.example
      <svg viewBox="0 0 16 16"><path d="M1 3 H15 V13 H1 Z"/><path d="M1.5 3.5 L8 9 L14.5 3.5" fill="none" stroke="var(--paper)" stroke-width="1.2"/></svg></li>
  </ul>
  <div class="tagline-band">Lawn &amp; Landscape Maintenance Services</div>
</section>

</body>
</html>
```